The Maplewood Kids Health Centre needs a Letterhead

We are a bilingual pediatric clinic located in Montreal, Canada.

Our english name is Maplewood Kids Health Centre
Our french name is Centre médical Bellerive

We offer complete care for children including general pediatric care, pediatric specialist care such as Ear, Nose and Throat, Urology, Neurology and Adolescent Medicine. We also have paramedical specialists such as psychologists, social workers, occupational therapists, speech and language pathologists.

The letterhead must use and be harmonious with our new logo. See Design #4923293. We need two types of letterhead. One for a the Logo and both english and french names on the top and the second with the list of current staff on the left. I have uploaded two old examples for you to see. Thanks and good luck.

Industry/Entity Type

Clinic

Font styles to use
Sans Serif

Colors
3176b5
9d9d9d

Requirements
Must have
• Include our logo.
Nice to have
• Most of our printing is done in black and white. So a grayscale design is fine.
I have included a color and grayscale versions of our logo.

We prefer clean modern designs.

```html
<!DOCTYPE html>
<html lang="en">
<head>
<meta charset="utf-8">
<title>Maplewood Kids Health Centre – Prescription Letterhead</title>
<link href="https://fonts.googleapis.com/css2?family=Didact+Gothic&display=swap" rel="stylesheet">
<style>
  :root {
    --backdrop: #e6e6e6;
    --paper: #ffffff;
    --ink: #6f6f6f;
    --ink-dark: #555555;
    --brand-grey: #9d9d9d;
    --band-grey: #7a7a7a;
    --rule: #8a8a8a;
  }
  * { box-sizing: border-box; margin: 0; padding: 0; }
  html, body { width: 1200px; height: 1000px; overflow: hidden; }
  body {
    background: var(--backdrop);
    font-family: "Didact Gothic", "Century Gothic", sans-serif;
    color: var(--ink);
    position: relative;
  }
  .letterhead {
    position: absolute;
    left: 252px; top: 40px;
    width: 696px; height: 920px;
    background: var(--paper);
    box-shadow: 0 6px 24px rgba(0,0,0,0.12);
    overflow: hidden;
  }
  .brand {
    position: absolute; left: 48px; top: 48px;
    display: flex; align-items: center; gap: 14px;
  }
  .brand-names { font-size: 17px; line-height: 1.05; color: var(--ink); }
  .brand-names.fr { text-align: right; }
  .brand-mark {
    width: 48px; height: 48px; border-radius: 50%;
    background: var(--brand-grey);
  }
  .physician {
    position: absolute; right: 48px; top: 46px; text-align: right;
  }
  .physician-name { font-size: 15px; color: var(--ink-dark); }
  .physician-title { font-size: 10px; letter-spacing: 0.5px; margin-top: 2px; }
  .physician-line { margin-top: 6px; width: 190px; border-bottom: 1px dotted var(--rule); margin-left: auto; }
  .field-grid {
    position: absolute; left: 48px; right: 48px; top: 132px;
    display: grid; grid-template-columns: 1fr 1fr; column-gap: 40px; row-gap: 14px;
    font-size: 12px;
  }
  .field { display: flex; align-items: flex-end; gap: 6px; }
  .field .dots { flex: 1; border-bottom: 1px dotted var(--rule); height: 10px; }
  .field .dots.short { flex: 0 0 90px; }
  .field .unit { font-size: 11px; }
  .contact {
    position: absolute; left: 0; right: 0; top: 206px;
    text-align: center; font-size: 11.5px; line-height: 1.45; color: var(--ink-dark);
  }
  .contact span + span { margin-left: 40px; }
  .header-rule {
    position: absolute; left: 48px; right: 48px; top: 248px;
    border-top: 2px solid var(--rule);
  }
  .side-band {
    position: absolute; right: 0; top: 420px; bottom: 0; width: 16px;
    background: var(--band-grey);
  }
  .side-mark {
    position: absolute; right: 24px; top: 318px;
    width: 100px; height: 100px; border-radius: 50%;
    background: var(--brand-grey); opacity: 0.85;
  }
  .repeat {
    position: absolute; right: 40px; bottom: 36px;
    display: flex; align-items: center; gap: 10px; font-size: 12px;
  }
  .repeat-box {
    width: 40px; height: 17px; border: 1px solid var(--rule);
    text-align: center; font-size: 11px; line-height: 15px;
  }
  .repeat-box.wide { width: 100px; }
</style>
</head>
<body>
  <main class="letterhead">
    <header>
      <div class="brand">
        <div class="brand-names fr">Centre<br>médical<br>Bellerive</div>
        <div class="brand-mark" aria-hidden="true"></div>
        <div class="brand-names en">Maplewood Kids<br>Health<br>Centre</div>
      </div>
      <div class="physician">
        <div class="physician-name">Daniel Morrow</div>
        <div class="physician-title">M.D., F.R.C.P. (C)</div>
        <div class="physician-line"></div>
      </div>
      <div class="field-grid">
        <div class="field"><span>Pour:</span><span class="dots"></span></div>
        <div class="field"><span>Adresse:</span><span class="dots"></span></div>
        <div class="field"><span>Date:</span><span class="dots"></span></div>
        <div class="field"><span>Poids:</span><span class="dots short"></span><span class="unit">kg.</span></div>
      </div>
      <div class="contact">
        <div>2210 Rue des Érables, Suite 100, Montréal, QC H3K 2B5</div>
        <div><span>Phone: (514) 555 0142</span><span>Fax: (514) 555 0177</span></div>
      </div>
      <div class="header-rule"></div>
    </header>
    <div class="side-mark" aria-hidden="true"></div>
    <div class="side-band" aria-hidden="true"></div>
    <footer class="repeat">
      <span>Repetatur:</span>
      <span class="repeat-box">1</span>
      <span class="repeat-box">2</span>
      <span class="repeat-box">3</span>
      <span class="repeat-box">4</span>
      <span class="repeat-box">5</span>
      <span class="repeat-box wide">NR</span>
    </footer>
  </main>
</body>
</html>
```